Resume: Professional Marketer seeking to impress potential recruiters with my skills & experience

Create a marketing esque style CV. I'm an outgoing, driven marketing with years of experience. I'm looking for a new senior role. My CV should look professional, but with elements of creativity and be a little bold. It should stand out amongst all the other CVs being submitted for a role. Check out my crewbase profile here: https://www.crewbase.example/in/marisol-tovrek-58210394/ I would like to include a photo with the design, as a subtle element of the design.

Target Market(s)

Recruiters, Headhunters

Industry/Entity Type

Marketing

Font styles to use
Sans Serif

Requirements
Must have
• Easy to read sections, with enough detail for a recruiter to understand my experience.
Nice to have
• Graphics, icons etc to represent experience

```html
<!DOCTYPE html>
<html lang="en">
<head>
<meta charset="utf-8">
<title>Career History – Senior Marketing Professional</title>
<link href="https://fonts.googleapis.com/css2?family=Libre+Caslon+Text:ital,wght@0,400;0,700;1,400&display=swap" rel="stylesheet">
<style>
  :root {
    --canvas: #ffffff;
    --paper: #e2d4c6;
    --paper-light: #e9ddd1;
    --paper-dark: #d8c8b8;
    --band: #efe6dc;
    --ink: #2a221d;
  }
  * { box-sizing: border-box; margin: 0; padding: 0; }
  html, body { width: 1200px; height: 850px; overflow: hidden; background: var(--canvas); }
  body {
    position: relative;
    font-family: "Libre Caslon Text", Georgia, serif;
    font-size: 10.2px;
    line-height: 12.8px;
    color: var(--ink);
  }
  .page {
    position: absolute;
    top: 14px;
    width: 584px;
    height: 826px;
    background:
      radial-gradient(ellipse at 30% 25%, var(--paper-light) 0%, transparent 60%),
      radial-gradient(ellipse at 75% 80%, var(--paper-dark) 0%, transparent 65%),
      var(--paper);
    box-shadow: 0 0 2px rgba(0,0,0,0.15);
  }
  .page--left { left: 10px; }
  .page--right { left: 606px; }
  .band {
    position: absolute;
    left: 0; width: 100%;
    height: 12px;
    background: var(--band);
  }
  .block {
    position: absolute;
    left: 40px;
    width: 520px;
    display: grid;
    grid-template-columns: 154px 1fr;
  }
  .label { grid-column: 1; }
  .content { grid-column: 2; }
  .row { display: contents; }
  .row + .row .label, .row + .row .content { margin-top: 9px; }
  .role-title { font-weight: 700; font-size: 10.4px; line-height: 14px; }
  .role-note { font-style: italic; font-size: 9.6px; }
  .content p + p, .content ol + p { margin-top: 4px; }
  ol { padding-left: 18px; margin-top: 2px; }
  ol li { margin-bottom: 3.8px; padding-left: 1px; }
  ol li::marker { font-size: 10px; }
  .rel-list li { list-style: none; margin-bottom: 4px; }
  .rel-list { padding: 0; }
</style>
</head>
<body>

<section class="page page--left">
  <div class="block" style="top:72px">
    <div class="row">
      <div class="label">March 2014 - August 2014</div>
      <div class="content">
        <div class="role-title">Head of Marketing &amp; General Manager - Business Operations<br>Meridian Life Distribution (UK) - Veralia Life, consumer life insurance brand</div>
        <div class="role-note">This role was a 3 month contract.</div>
      </div>
    </div>
    <div class="row">
      <div class="label">Role responsibilities:</div>
      <div class="content">
        <p>The overarching objectives of the 3 month relocation to London were to:</p>
        <ol>
          <li>To prepare MLD UK for the launch of the Direct Life Insurance brand.</li>
          <li>To leave the MLD UK in a prepared position for the CEO &amp; MLD team to successfully launch the brand to the agreed timeline.</li>
        </ol>
        <p>The primary objectives of the General Manager Marketing &amp; Business Operations:</p>
        <ol>
          <li>To obtain financial services license for MLD (Direct Authorisation &amp; Appointed Rep Status)</li>
          <li>To establish the Sales Call Centre front end &amp; lead management processes</li>
          <li>To develop the Acquisition Plan to meet the Year 1 Sales unit targets, within budget</li>
          <li>To shortlist Creative Agencies for selection by the CEO, UK</li>
          <li>To shortlist Marketing roles and Support roles for selection by the CEO, UK</li>
          <li>To develop the project plan, and to understand and outline the critical path</li>
          <li>Develop relationships and pursue engagement with all external business partners; including, Marketing Suppliers, Call Centre Operators, the Insurer and their Consultants, Printers and Mail houses, Telephony providers, Recruiters, Banks, external Legal Counsel, Compliance Consultants, IT providers.</li>
          <li>General administration of a start up company overseas</li>
        </ol>
      </div>
    </div>
  </div>

  <div class="block" style="top:492px">
    <div class="label">Reporting to:<br>Key Relationships:</div>
    <div class="content">Reporting to: Group CEO, Meridian Life Distribution<br>Key stakeholder relationships with;<br>Five owners of Meridian Life Distributions, including Halvard Re UK</div>
  </div>

  <div class="band" style="top:546px"></div>

  <div class="block" style="top:570px">
    <div class="row">
      <div class="label">December 2012 - May 2013</div>
      <div class="content"><div class="role-title">Commercial &amp; MIS Advisor<br>Korvel Limited</div></div>
    </div>
    <div class="row">
      <div class="label">Role responsibilities:</div>
      <div class="content">
        <p>The primary objectives of the Commercial &amp; MIS Advisor / Manager are to;</p>
        <ol>
          <li>Deliver commercial insights and advise the Senior Management Team regularly in all areas of the business including; Acquisition, the existing book (customers), financial performance, and the external environment</li>
          <li>Direct the development and implementation of Management Information Solutions and Systems for Korvel Direct</li>
          <li>Direct the development of commercial modeling for Korvel Direct including; Acquisition, Retention, Claims, Policy Administration, corporate overheads</li>
        </ol>
      </div>
    </div>
  </div>
</section>

<section class="page page--right">
  <div class="block" style="top:72px">
    <div class="content">
      <ol start="4" style="margin-top:0">
        <li>Produce and communicate the Financial statements and supporting insights to inform future performance decisions</li>
        <li>Direct the management and implementation of reporting solutions for Korvel Direct Acquisition and Retention</li>
        <li>Direct the implementation of projects impacting all aspects of Marketing</li>
      </ol>
      <p>The Head of Marketing Operations engages with senior leadership; delivering outcomes by influencing and leading others.</p>
    </div>
  </div>

  <div class="block" style="top:207px">
    <div class="label">Reporting to:<br>Key Relationships:</div>
    <div class="content">
      <ul class="rel-list">
        <li>Chief Marketing Officer</li>
        <li>New Ventures Director (formerly Joint Chief Operating Officer)</li>
        <li>Commercial Director (formerly Joint Chief Operating Officer)</li>
        <li>GM Call Centre Operations</li>
        <li>Marketing Leadership Team</li>
        <li>Head of Sales</li>
      </ul>
    </div>
  </div>

  <div class="band" style="top:318px"></div>

  <div class="block" style="top:349px">
    <div class="row">
      <div class="label">October 2010 - July 2012</div>
      <div class="content"><div class="role-title">P&amp;L / Brand Manager – CoverPath<br>Part of the ASHFORD Group</div></div>
    </div>
    <div class="row">
      <div class="label">Role responsibilities:</div>
      <div class="content">
        <p>The primary objectives of the P&amp;L / Brand Manager – CoverPath:</p>
        <ol style="padding-left:14px">
          <li>To deliver revenue to achieve CoverPath Direct growth objectives</li>
          <li>To manage costs to achieve CoverPath Direct profit objectives</li>
          <li>To actively drive strategic projects within CoverPath Direct, which contribute to either revenue or profit objectives, or both</li>
          <li>To contribute to the delivery of the revenue &amp; profit objectives of the Alliance partners</li>
          <li>To develop strategies for CoverPath and the broader Direct business, by understanding how CoverPath fits within ASHFORD Group</li>
          <li>Budget preparation, management monthly &amp; accountability</li>
          <li>Reporting of the P&amp;L</li>
          <li>Engage key internal stakeholders to ensure financial objectives are achieved</li>
        </ol>
      </div>
    </div>
  </div>

  <div class="block" style="top:663px">
    <div class="label">Reporting to:<br>Key Relationships:</div>
    <div class="content">Key stakeholder relationships with;<br>Three P&amp;L / Brand Managers – Alliance Partners<br>Two Joint CEO<br>Head of Sales<br>Head of Product<br>Head of Marketing</div>
  </div>
</section>

</body>
</html>
```